Business Card Design Project

We are an agricultural business based in Brisbane.
We design, manage and operate regional saleyards. Our logo is green/silver in colour and details of our business can be found on our website www.vodemarketyards.com.au

Just wanting a corporate design for some business cards and include name, position, contact details.

Thanks

Industry/Entity Type

Business

```html
<!DOCTYPE html>
<html lang="en">
<head>
<meta charset="utf-8">
<title>Vode Market Yards – Business Card</title>
<link rel="stylesheet" href="https://fonts.googleapis.com/css2?family=Open+Sans:wght@400;600;700;800&display=swap">
<style>
  :root {
    --green-deep: #0f4a1c;
    --green-mid: #1a5e27;
    --green-accent: #1f9a4a;
    --silver: #eeeeee;
    --silver-dark: #8a8a8a;
    --white: #ffffff;
    --text-soft: #d9e6db;
    --page: #ecebe8;
  }
  * { box-sizing: border-box; margin: 0; padding: 0; }
  html, body { width: 1200px; height: 960px; overflow: hidden; }
  body {
    background: var(--page);
    font-family: "Open Sans", Arial, sans-serif;
    display: flex; flex-direction: column; align-items: center; justify-content: center;
    gap: 50px;
  }
  .card {
    position: relative; width: 700px; height: 400px; overflow: hidden;
    background: radial-gradient(ellipse at 60% 40%, var(--green-mid), var(--green-deep));
    box-shadow: 0 6px 18px rgba(0,0,0,.18);
  }
  .card__shape { position: absolute; inset: 0; width: 100%; height: 100%; }
  .brand {
    position: absolute; color: var(--green-deep);
    font-weight: 800; text-transform: uppercase; line-height: 1.05; letter-spacing: .5px;
  }
  .card--front .brand { left: 28px; top: 110px; font-size: 26px; }
  .card--back .brand { left: 0; right: 0; top: 166px; text-align: center; font-size: 32px; }
  .details { position: absolute; left: 400px; top: 52px; width: 270px; color: var(--white); }
  .details__name { font-size: 27px; font-weight: 700; letter-spacing: .3px; }
  .details__rule { height: 1px; background: rgba(255,255,255,.45); margin: 8px 0; }
  .details__title { font-size: 13px; color: var(--text-soft); padding-left: 14px; position: relative; }
  .details__list { list-style: none; margin-top: 22px; font-size: 12px; line-height: 1.65; color: var(--text-soft); }
  .details__list li { padding-left: 18px; position: relative; }
  .details__list li.bullet::before,
  .details__title::before {
    content: ""; position: absolute; left: 2px; top: 7px;
    border-left: 4px solid transparent; border-right: 4px solid transparent;
    border-top: 5px solid var(--text-soft);
  }
  .details__list li.gap { margin-top: 10px; }
</style>
</head>
<body>

<section class="card card--front" aria-label="Business card front">
  <svg class="card__shape" viewBox="0 0 700 400" aria-hidden="true">
    <polygon points="0,0 360,0 80,400 0,400" fill="var(--silver)"/>
    <polygon points="360,0 372,0 92,400 80,400" fill="var(--green-accent)"/>
  </svg>
  <div class="brand">Vode Market<br>Yards</div>
  <div class="details">
    <h1 class="details__name">Daniel Whitford</h1>
    <div class="details__rule"></div>
    <p class="details__title">Chief Executive Officer - VMY</p>
    <div class="details__rule"></div>
    <ul class="details__list">
      <li class="bullet">Australia</li>
      <li>27 Saleyard Road, Suite 8</li>
      <li>Brisbane, QLD 4000</li>
      <li class="bullet gap">Email: daniel@vodemarketyards.com.au</li>
      <li>Mob: 0400 555 217</li>
      <li>www.vodemarketyards.com.au</li>
    </ul>
  </div>
</section>

<section class="card card--back" aria-label="Business card back">
  <svg class="card__shape" viewBox="0 0 700 400" aria-hidden="true">
    <polygon points="20,200 350,110 680,200 350,290" fill="var(--silver)"/>
    <polygon points="20,200 350,290 680,200 680,210 350,300 20,210" fill="var(--green-accent)"/>
  </svg>
  <div class="brand">Vode Market<br>Yards</div>
</section>

</body>
</html>
```